Ferncastle Financial - Website Design

We need a website design for a new commercial real estate company called Ferncastle Financial. We're effectively commercial mortgage brokers connecting real estate investors to lenders. We need a website that is simple (not busy), elegant, professional, and user-friendly. A lot of the users will be in their 50's and less tech savvy, so a stream-lined design is best. The website will serve as a portal for lenders to review new financing opportunities, as well as for real estate investors to review terms from lenders.
Updates
Just uploaded our logo.
Target Market(s)
Commercial real estate investors and lenders
Industry/Entity Type
Real Estate
Number of Pages Required
1 page
Colors
Designer to choose colors to be used in the design.
Look and feel

```html
<!DOCTYPE html>
<html lang="en">
<head>
<meta charset="utf-8">
<title>Ferncastle Financial</title>
<link rel="stylesheet" href="https://fonts.googleapis.com/css2?family=Lato:wght@300;400;700;900&family=Open+Sans:wght@400;600;700&family=Raleway:wght@600&display=swap">
<style>
:root{
  --navy:#1b2a47;
  --hero-blue:#2a5aa8;
  --hero-blue-deep:#1f4a92;
  --yellow:#f5be1e;
  --green:#27ae4f;
  --light:#f1f1f1;
  --band:#ececec;
  --text:#333;
  --muted:#777;
  --white:#fff;
}
*{margin:0;padding:0;box-sizing:border-box}
html,body{width:1200px;height:2305px;overflow:hidden}
body{position:relative;font-family:"Open Sans",Arial,sans-serif;color:var(--text);background:var(--white)}

/* Hero */
.hero{position:absolute;left:0;top:0;width:1200px;height:635px;overflow:hidden}
.hero-photo{position:absolute;inset:0;background:
  radial-gradient(ellipse 380px 460px at 760px 330px,rgba(90,140,205,.55),transparent 70%),
  linear-gradient(100deg,var(--hero-blue-deep) 0%,var(--hero-blue) 45%,#3465b3 75%,#2b5ba8 100%)}
.brand{position:absolute;left:129px;top:0;width:152px;height:118px;background:var(--white);display:flex;flex-direction:column;align-items:center;justify-content:center;gap:8px}
.brand-dot{width:34px;height:34px;border-radius:50%;background:var(--navy)}
.brand-name{font-family:"Lato",sans-serif;font-weight:700;font-size:15px;color:var(--navy);letter-spacing:.5px;text-align:center;line-height:1.1}
.main-nav{position:absolute;top:30px;left:552px;display:flex}
.main-nav a{font-family:"Open Sans",sans-serif;font-size:15px;color:var(--white);text-decoration:none;margin-right:30px;position:relative}
.main-nav a.active::before{content:"";position:absolute;left:0;right:0;top:-30px;height:4px;background:var(--navy)}
.hero-title{position:absolute;left:130px;top:250px;font-family:"Lato",sans-serif;font-weight:400;font-size:54px;line-height:54px;color:var(--white)}
.hero-title b{font-weight:900}
.hero-sub{position:absolute;left:130px;top:368px;font-family:"Open Sans",sans-serif;font-weight:600;font-size:22px;color:var(--white)}
.btn{display:inline-flex;align-items:center;justify-content:center;font-family:"Open Sans",sans-serif;font-weight:700;text-transform:uppercase;color:var(--white);background:var(--yellow);text-decoration:none}
.hero-btn{position:absolute;left:132px;top:418px;width:168px;height:52px;border-radius:5px;font-size:16px}

/* Featured */
.featured{position:absolute;left:0;top:635px;width:1200px;height:567px;background:var(--light)}
.section-title{font-family:"Lato",sans-serif;font-weight:400;font-size:30px;color:#333;text-align:center}
.featured .section-title{position:absolute;top:44px;width:100%}
.featured-intro{position:absolute;top:84px;left:300px;width:600px;text-align:center;font-size:15.5px;line-height:23px;color:#666}
.listing{position:absolute;top:159px;width:309px;height:343px;background:var(--white)}
.listing-photo{height:190px}
.fav{position:absolute;right:12px;top:12px;width:32px;height:32px;border-radius:50%;background:var(--white);display:flex;align-items:center;justify-content:center}
.listing-name{position:absolute;left:17px;top:204px;font-size:14px;font-weight:600;color:#222}
.listing-addr{position:absolute;left:17px;top:226px;font-size:10.5px;color:#999;display:flex;align-items:center;gap:3px}
.listing-price{position:absolute;left:17px;top:248px;font-size:14px;font-weight:700;color:var(--green)}
.listing-price small{font-size:11px;font-weight:400}
.stats{position:absolute;left:17px;top:287px;display:flex;gap:14px}
.stat b{display:block;font-size:17px;font-weight:400;color:#222;line-height:18px}
.stat b sup{font-size:10px}
.stat span{display:block;font-size:7px;color:#666;letter-spacing:.5px;margin-top:3px}
.details{position:absolute;right:19px;top:288px;width:115px;height:32px;border:1.5px solid var(--green);border-radius:16px;font-size:11px;color:var(--green);display:flex;align-items:center;justify-content:center;text-transform:uppercase}

/* About */
.about{position:absolute;left:0;top:1202px;width:1200px;height:425px;overflow:hidden}
.about-photo{position:absolute;inset:0;background:linear-gradient(90deg,#241a14 0%,#3b2c22 30%,#5a4436 60%,#3a2b22 100%)}
.agent-photo{position:absolute;left:230px;top:22px;width:266px;height:403px;background:linear-gradient(180deg,#2c3650 0%,#222c46 100%)}
.about-title{position:absolute;left:542px;top:122px;font-family:"Lato",sans-serif;font-weight:400;font-size:29px;color:var(--white)}
.about-text{position:absolute;left:542px;top:168px;width:480px;font-size:15px;line-height:22px;color:#eee}
.about-btn{position:absolute;left:542px;top:270px;width:157px;height:40px;font-size:15px}

/* Testimonial */
.video{position:absolute;left:111px;top:1689px;width:476px;height:287px;background:linear-gradient(120deg,#4a4a4a,#6b6b6b 50%,#555)}
.play{position:absolute;left:214px;top:120px}
.clients-title{position:absolute;left:612px;top:1686px;font-family:"Raleway",sans-serif;font-weight:600;font-size:23px;color:#222}
.quote{position:absolute;left:612px;top:1736px;width:476px;height:123px;background:var(--light);padding:24px 26px;font-size:11px;line-height:18px;color:#555}
.quote::after{content:"";position:absolute;left:30px;bottom:-12px;border:12px solid transparent;border-top-color:var(--light);border-bottom:0}
.avatar{position:absolute;left:615px;top:1887px;width:64px;height:64px;border-radius:50%;background:linear-gradient(135deg,#c9b39b,#8a7766)}
.client-name{position:absolute;left:698px;top:1884px;font-size:14px;font-weight:600;color:#222}
.client-place{position:absolute;left:698px;top:1907px;font-size:11.5px;color:#999}
.stars{position:absolute;left:698px;top:1928px;font-size:12px;color:#f0a500;letter-spacing:1px}

/* Partners */
.partners{position:absolute;left:0;top:2036px;width:1200px;height:103px;background:var(--band);display:flex;align-items:center;justify-content:space-around;padding:0 110px}
.partner{display:flex;align-items:center;gap:10px;font-family:"Open Sans",sans-serif;font-weight:600;font-size:26px;color:#7b7b7b}
.partner i{width:18px;height:18px;background:#8a8a8a;display:block}

/* Footer */
.site-footer{position:absolute;left:0;top:2139px;width:1200px;height:166px;background:var(--navy);color:var(--white);text-align:center}
.social{position:absolute;top:34px;left:0;width:100%;display:flex;justify-content:center;gap:11px}
.social span{width:35px;height:35px;border-radius:50%;background:#8a8f99;display:block}
.footer-nav{position:absolute;top:88px;width:100%;display:flex;justify-content:center;gap:26px}
.footer-nav a{color:var(--white);text-decoration:none;font-size:13.5px}
.copyright{position:absolute;top:114px;width:100%;font-size:12.5px}
</style>
</head>
<body>

<header class="hero">
  <div class="hero-photo" role="img" aria-label="Smiling couple holding house keys, blue-toned photograph"></div>
  <div class="brand"><span class="brand-dot"></span><span class="brand-name">Ferncastle<br>Financial</span></div>
  <nav class="main-nav">
    <a href="#" class="active">HOME</a><a href="#">SERVICE</a><a href="#">PROPERTIES</a><a href="#">AGENT</a><a href="#">BLOG</a><a href="#">CONTACT US</a>
  </nav>
  <h1 class="hero-title">WANT TO BUY<br><b>OR RENT</b> HOME ?</h1>
  <p class="hero-sub">FERNCASTLE SOLVE YOUR PROBLEMS</p>
  <a href="#" class="btn hero-btn">Contact Us</a>
</header>

<section class="featured">
  <h2 class="section-title">FEATURED LISTING</h2>
  <p class="featured-intro">Lorem consectetur adipiscing elit, sed do eiusmod tempor dolor sit amet contetur adipiscing elit, sed do eiusmod tempor incididunt</p>

  <article class="listing" style="left:112px">
    <div class="listing-photo" role="img" aria-label="Victorian villa with garage at dusk" style="background:linear-gradient(180deg,#6a6aa8 0%,#a58aa8 35%,#8a7a6a 65%,#3d4a2c 100%)"></div>
    <span class="fav"><svg width="14" height="13" viewBox="0 0 14 13"><path d="M7 12 1.5 6.5A3 3 0 0 1 7 2.5a3 3 0 0 1 5.5 4Z" fill="none" stroke="#999" stroke-width="1.2"/></svg></span>
    <h3 class="listing-name">Real House Luxury Villa</h3>
    <p class="listing-addr"><svg width="7" height="10" viewBox="0 0 7 10"><path d="M3.5 10S0 5.5 0 3.5a3.5 3.5 0 0 1 7 0C7 5.5 3.5 10 3.5 10Z" fill="#bbb"/></svg>42 Elm Grove Ave, 12 - Riverside North, Ashford</p>
    <p class="listing-price">$2,285,500</p>
    <div class="stats"><div class="stat"><b>5<sup>+</sup></b><span>BEDS</span></div><div class="stat"><b>3</b><span>BATHS</span></div><div class="stat"><b>1,250</b><span>SQ.FT</span></div></div>
    <span class="details">Details &rsaquo;</span>
  </article>

  <article class="listing" style="left:446px">
    <div class="listing-photo" role="img" aria-label="Modern house with lit pool at night" style="background:linear-gradient(180deg,#2a2e38 0%,#4a4640 45%,#8a6a44 65%,#2f8ad0 85%,#1a5a8a 100%)"></div>
    <span class="fav"><svg width="14" height="13" viewBox="0 0 14 13"><path d="M7 12 1.5 6.5A3 3 0 0 1 7 2.5a3 3 0 0 1 5.5 4Z" fill="none" stroke="#999" stroke-width="1.2"/></svg></span>
    <h3 class="listing-name">House Take Away</h3>
    <p class="listing-addr"><svg width="7" height="10" viewBox="0 0 7 10"><path d="M3.5 10S0 5.5 0 3.5a3.5 3.5 0 0 1 7 0C7 5.5 3.5 10 3.5 10Z" fill="#bbb"/></svg>42 Elm Grove Ave, 12 - Riverside North, Ashford</p>
    <p class="listing-price">$85,500/ <small>Month</small></p>
    <div class="stats"><div class="stat"><b>5<sup>+</sup></b><span>BEDS</span></div><div class="stat"><b>3</b><span>BATHS</span></div><div class="stat"><b>1,250</b><span>SQ.FT</span></div></div>
    <span class="details">Details &rsaquo;</span>
  </article>

  <article class="listing" style="left:780px">
    <div class="listing-photo" role="img" aria-label="White modern villa with swimming pool and lawn" style="background:linear-gradient(180deg,#5a9ad8 0%,#cfd8de 40%,#e6e6e2 55%,#2aa0c8 75%,#5a8a3a 100%)"></div>
    <span class="fav"><svg width="14" height="13" viewBox="0 0 14 13"><path d="M7 12 1.5 6.5A3 3 0 0 1 7 2.5a3 3 0 0 1 5.5 4Z" fill="none" stroke="#999" stroke-width="1.2"/></svg></span>
    <h3 class="listing-name">Weston Hightpointe Place</h3>
    <p class="listing-addr"><svg width="7" height="10" viewBox="0 0 7 10"><path d="M3.5 10S0 5.5 0 3.5a3.5 3.5 0 0 1 7 0C7 5.5 3.5 10 3.5 10Z" fill="#bbb"/></svg>42 Elm Grove Ave, 12 - Riverside North, Ashford</p>
    <p class="listing-price">REQUEST PRICE</p>
    <div class="stats"><div class="stat"><b>5<sup>+</sup></b><span>BEDS</span></div><div class="stat"><b>3</b><span>BATHS</span></div><div class="stat"><b>1,250</b><span>SQ.FT</span></div></div>
    <span class="details">Details &rsaquo;</span>
  </article>
</section>

<section class="about">
  <div class="about-photo" role="img" aria-label="Stone house exterior lit at night"></div>
  <div class="agent-photo" role="img" aria-label="Photo of a real estate agent in a suit"></div>
  <h2 class="about-title">SOME WORD ABOUT FERNCASTLE</h2>
  <p class="about-text">Lorem consectetur adipiscing elit, sed do eiusmod tempor dolor sit amet contetur adipiscing elit, sed do eiusmod tempor inc ididunt quis nostrud exercitation oris nisi ut aliquip.</p>
  <a href="#" class="btn about-btn">Read More</a>
</section>

<div class="video" role="img" aria-label="Video still of a couple holding a house sign">
  <svg class="play" width="48" height="48" viewBox="0 0 48 48"><circle cx="24" cy="24" r="21" fill="rgba(255,255,255,.15)" stroke="#fff" stroke-width="3"/><path d="M19 14 34 24 19 34Z" fill="#fff"/></svg>
</div>
<h2 class="clients-title">2000+ Happy Clients</h2>
<blockquote class="quote">Homevale has recently sold our house and home. We have found that it was one of the best investments we could have made, as nothing was a problem to her, and it certainly took the worry of marketing and selling off our mind, as Homevale had everything under control.</blockquote>
<div class="avatar" role="img" aria-label="Client portrait"></div>
<p class="client-name">Dana &amp; Theo</p>
<p class="client-place">Ashford, Millbrook</p>
<p class="stars">★★★★★</p>

<section class="partners" aria-label="Partners">
  <span class="partner">nordly<i></i></span>
  <span class="partner">brightam</span>
  <span class="partner"><i></i>veloria</span>
  <span class="partner">CASTWELL</span>
  <span class="partner"><i></i>orbis</span>
</section>

<footer class="site-footer">
  <div class="social" aria-label="Social links"><span></span><span></span><span></span><span></span><span></span></div>
  <nav class="footer-nav"><a href="#">Home</a><a href="#">Purchase Tips</a><a href="#">Refinance Tips</a><a href="#">Blog</a><a href="#">About Us</a></nav>
  <p class="copyright">© 2017 Ferncastle Financial - &nbsp;Privacy Policy</p>
</footer>

</body>
</html>
```